German CBD company needs a label+packaging design (templates provided)

Hey there,
we are a German e-commerce company and about to launch a CBD E-liquid series under our new brand "VELMORIQ". We need designs for the cardbord tube packaging and the labels of bottles. Find attached templates for both, the labels and the packaging. The templates already have a design on them just for you to know that some space will be filled with legal information. Feel free to use the templates and change the designs and of course we have the suitable text down below. Every outer packaging label and bottle label should include the brand name "VELMORIQ" (we typically use the font Archivo Black, but feel free to change it, if you have a better idea), the CBD content, the flavour and the filling quantity (10ml). You can use 100mg and Mango for your design and if your design wins, we will work with you and change the flavours and concentrations for the other liquids accordingly. Our liquids are Made in Germany and of a very high quality so we are looking for a premium design that underlines the quality und purity of our product. Something between luxurious and futuristic. Please let your creativity run wild :)

As for the packaging we need the following texts on the packaging:

DE:
(bold)Inhaltsstoffe:(bold) < 70% Propylen Glycol, < 30% VG Glycerol, Aromen, Cannabidiol (CBD) wie angegeben CAS 13956-29-1.
(bold)Anwendung(bold) Vor Benutzung schütteln. Dieses Produkt ist unverdünnt in einer kompatiblen e-Zigarette anzuwenden. 2-3 Züge inhalieren. Zwischen den Anwendungen 10-20 Minuten warten. Dieses Produkt ersetzt keine ausgewogene Ernährung.
(bold)Hinweise:(bold) VELMORIQ CBD e-Liquids sind Tabakersatzprodukte gem. TPD2 und bestehen aus organischen und zertifizierten, >99% reinen CBD-Kristallen. HACCP & GMP konform. Nicht empfohlen für Schwangere, stillende Frauen oder Nichtraucher. Dieses Produkt ist nicht zur Diagnose, Behandlung, Heilung oder Vorbeugung von Krankheiten bestimmt. Darf nicht in die Hände von Kindern und Jugendlichen gelangen. Keine Abgabe unter 18 Jahren. Dunkel und kühl lagern. Nicht zum Verzehr geeignet.

EN:
(bold)Ingredients:(bold) < 70% Propylen Glycol, < 30% VG Glycerol, flavours , Cannabidiol (CBD).
(bold)Application(bold): Shake before use. This product should be applied undiluted in a compatible e-cigarette. Inhale 2-3 puffs. Wait 10-20 minutes until using again.
(bold)Notes(bold): VELMORIQ e-liquids are made from organic and certified >99% pure CBD Crystals. HACCP & GMP compliant. Not recommended for pregnant or breastfeeding women or non-smokers.
This product is not intended to diagnose, treat, cure or prevent any disease. Keep away from children. No sale to minors. Store in a cool, dark place. Not for consumption.

DE: Qualität:
Wir verwenden für unsere Liquids organische und zertifizierte CBD-Kristalle von >99% Reinheit. Wir verwenden nur die hochwertigsten Rohstoffe zur Herstellung unserer Liquids, um unseren Kunden ein optimales Vape-Erlebnis bieten zu können.
EN: Quality:
We use organic and certified CBD-Crystals with a purity >99%. We only use the highest quality raw material for the production of our liquids in order to ensure an optimal vaping experience for our customers.

Please consider that we will also need space for our contact information, our website URL and an EAN bar code.

Now the label for the bottles: As already said our templates have designs on them, so please feel free to change anything you like. It`s just an example of the label printing company so we could get an idea. We just need the following texts on those labels:
DE:(bold)Inhaltsstoffe:(bold) < 70% Propylen Glycol, < 30% VG Glycerol, Aromen, Cannabidiol (CBD) wie angegeben CAS 13956-29-1.
Darf nicht in die Hände von Kindern und Jugendlichen gelangen. Keine Abgabe unter 18 Jahren.

EN:(bold)Ingredients:(bold) < 70% Propylen Glycol, < 30% VG Glycerol, flavours , Cannabidiol (CBD).
Keep away from children. No sale to minors.
Moreover, we need the symbols that are already on the label and some space for an EAN bar code. The labels should include CBD content, brand name, flavour..(see above)

I hope our briefing is clear enough. If you have any further questions, please contact me via e-mail (olek.dravin@quenlo-shop.example).
We are looking forwards to receiving your designs and doing some further work with you. We know that it`s more than one simple task, so we are willing to pay a little bonus for the further work which we will do with the winner :)

Greetings from Frankfurt, Germany
Quenlo GmbH Team
Olek Dravin
olek.dravin@quenlo-shop.example

Font styles to use
Other font styles liked:
• Archivo Black (not mandatory, just an idea)

Colors

Designer to choose colors to be used in the design.

Requirements
Must have
• - Legal notices as mentioned above
• - CBD content in mg
• - flavour
• - space for EAN bar code & contact information
Should not have
• - shouldn`t look too clean, not like a medicine

```html
<!DOCTYPE html>
<html lang="en">
<head>
<meta charset="utf-8">
<title>VELMORIQ CBD Eliquid – Bottle Label</title>
<link href="https://fonts.googleapis.com/css2?family=Archivo+Black&family=Montserrat:ital,wght@0,400;0,500;0,700;1,500&display=swap" rel="stylesheet">
<style>
  :root {
    --page: #e9e9e9;
    --label-black: #121212;
    --panel-grey: #2a2a2a;
    --gold: #d9a62e;
    --gold-light: #f2c95a;
    --gold-dark: #a87a17;
    --white: #f5f5f5;
    --ink: #1a1a1a;
    --flag-red: #d52b1e;
  }
  * { box-sizing: border-box; margin: 0; padding: 0; }
  html, body { width: 750px; height: 1200px; overflow: hidden; }
  body {
    background: var(--page);
    font-family: "Montserrat", Arial, sans-serif;
    position: relative;
  }
  .label-sheet {
    position: absolute;
    left: 0; top: 380px;
    width: 750px; height: 440px;
    background: var(--panel-grey);
  }
  .label {
    position: absolute;
    left: 15px; top: 22px;
    width: 720px; height: 396px;
    background: var(--label-black);
    overflow: hidden;
  }
  .legal {
    position: absolute;
    left: 28px; top: 34px;
    width: 205px;
    color: var(--white);
    font-size: 10.5px;
    line-height: 1.42;
  }
  .legal p { margin-bottom: 12px; }
  .legal b { font-weight: 700; }
  .contact {
    color: var(--gold);
    font-size: 10px;
    line-height: 1.4;
    font-weight: 500;
  }
  .contact-title { font-weight: 700; font-size: 11px; }
  .symbols {
    position: absolute;
    left: 28px; top: 322px;
    display: flex; gap: 8px; align-items: center;
  }
  .brand-band {
    position: absolute;
    left: 248px; top: 0;
    width: 58px; height: 396px;
    background: linear-gradient(90deg, var(--gold-dark), var(--gold-light) 50%, var(--gold-dark));
    display: flex; align-items: center; justify-content: center;
  }
  .brand-name {
    font-family: "Archivo Black", Arial, sans-serif;
    color: var(--ink);
    font-size: 44px;
    letter-spacing: 3px;
    transform: rotate(-90deg);
    white-space: nowrap;
  }
  .product {
    position: absolute;
    left: 330px; top: 0;
    width: 360px; height: 396px;
    text-align: center;
    color: var(--white);
  }
  .brand-dot {
    width: 30px; height: 30px;
    border-radius: 50%;
    background: var(--gold);
    margin: 52px auto 14px;
  }
  .product-type {
    font-weight: 500;
    font-size: 58px;
    line-height: 1;
    letter-spacing: 2px;
  }
  .product-line {
    font-weight: 500;
    font-size: 50px;
    line-height: 1.1;
    letter-spacing: 2px;
  }
  .rule {
    width: 300px; height: 2px;
    background: var(--gold);
    margin: 20px auto 24px;
  }
  .flavour {
    display: inline-block;
    background: linear-gradient(90deg, var(--gold-dark), var(--gold-light), var(--gold-dark));
    color: var(--ink);
    font-style: italic;
    font-weight: 500;
    font-size: 20px;
    padding: 6px 60px 6px 18px;
    margin-left: 120px;
  }
  .content {
    margin-top: 24px;
    font-size: 18px;
    font-weight: 500;
    letter-spacing: 1px;
    text-align: right;
    padding-right: 30px;
  }
</style>
</head>
<body>
  <section class="label-sheet">
    <div class="label">
      <div class="legal">
        <p><b>DE: Inhaltsstoffe:</b> &lt; 70% Propylen Glycol, &lt; 30% VG Glycerol, Aromen, Cannabidiol (CBD) wie angegeben CAS 13956-29-1. Darf nicht in die Hände von Kindern und Jugendlichen gelangen. Keine Abgabe unter 18 Jahren.</p>
        <p><b>EN: Ingredients:</b> &lt; 70% Propylen Glycol, &lt; 30% VG Glycerol, flavours, Cannabidiol (CBD). Keep away from children. No sale to minors.</p>
        <div class="contact">
          <div class="contact-title">CONTACT INFORMATION</div>
          <div>48 LINDEN COURT, SUITE 12, HARLOW, NV</div>
          <div>20417 TEL: 555-014-2290 FAX: 555-014-2291</div>
          <div>INFO@VELMORIQ-MAIL.EXAMPLE</div>
        </div>
      </div>
      <div class="symbols">
        <svg width="34" height="34" viewBox="0 0 34 34" role="img" aria-label="Age restriction badge">
          <circle cx="17" cy="17" r="15" fill="var(--white)" stroke="var(--flag-red)" stroke-width="3"/>
        </svg>
        <svg width="34" height="34" viewBox="0 0 34 34" role="img" aria-label="Pregnancy warning badge">
          <circle cx="17" cy="17" r="15" fill="var(--white)" stroke="var(--flag-red)" stroke-width="3"/>
        </svg>
        <svg width="34" height="34" viewBox="0 0 34 34" role="img" aria-label="Made in Germany flag">
          <circle cx="17" cy="17" r="16" fill="var(--white)"/>
          <clipPath id="flag-clip"><circle cx="17" cy="17" r="13"/></clipPath>
          <g clip-path="url(#flag-clip)">
            <rect x="0" y="4" width="34" height="9" fill="#000"/>
            <rect x="0" y="13" width="34" height="9" fill="var(--flag-red)"/>
            <rect x="0" y="22" width="34" height="9" fill="#ffce00"/>
          </g>
        </svg>
      </div>
      <div class="brand-band">
        <span class="brand-name">VELMORIQ</span>
      </div>
      <div class="product">
        <div class="brand-dot"></div>
        <div class="product-type">CBD</div>
        <div class="product-line">ELIQUID</div>
        <div class="rule"></div>
        <div class="flavour">Mango Flavour</div>
        <div class="content">100MG | 10ML CBD</div>
      </div>
    </div>
  </section>
</body>
</html>
```